Billboard design for a jewelry store.

I am looking for a very unique design with a catchy slogan, I am looking for billboard so good that will make the front page of the newspaper. I want to target customers that are looking for diamond jewelry or diamonds in general. For sure not interested in anything that is genetic or been used in the past. I want the billboard to stand out and very unique. Text not more than 3 words, our logo and an image.

Target Market(s)

Local

Industry/Entity Type

Jewelry Store

Font styles to use
Other font styles liked:
• Open to your suggestion for the font.

Requirements
Must have
• Unique, very brief a catchy slogan. My logo and an image. Open for suggestions. I want also different formats to use on social media.
Nice to have
• I am open to unique and amazing new ideas. I don't want general used design or slogan.
Should not have
• Too much text

```html
<!DOCTYPE html>
<html lang="en">
<head>
<meta charset="utf-8">
<title>Vella Jewelers Billboard</title>
<link rel="stylesheet" href="https://fonts.googleapis.com/css2?family=Cinzel:wght@700&display=swap">
<style>
  :root {
    --page: #ffffff;
    --panel-white: #ffffff;
    --panel-mist: #e6e9f2;
    --navy-deep: #1f2a4a;
    --navy: #2f3d66;
    --steel-blue: #5b6ca8;
    --ice: #c9d3f2;
    --ink: #111111;
  }
  html, body {
    margin: 0;
    padding: 0;
    width: 1200px;
    height: 1199px;
    overflow: hidden;
    background: var(--page);
  }
  .canvas {
    position: relative;
    width: 1200px;
    height: 1199px;
  }
  .billboard {
    position: absolute;
    left: 30px;
    top: 413px;
    width: 1140px;
    height: 373px;
    box-shadow: 0 4px 14px rgba(0,0,0,0.25);
  }
  .billboard svg { display: block; width: 100%; height: 100%; }
  .brand-name {
    font-family: "Cinzel", "Times New Roman", serif;
    font-weight: 700;
    fill: var(--ink);
  }
</style>
</head>
<body>
<main class="canvas">
  <section class="billboard">
    <svg viewBox="0 0 800 262" preserveAspectRatio="none" xmlns="http://www.w3.org/2000/svg">
      <defs>
        <linearGradient id="navyField" x1="0" y1="0" x2="1" y2="1">
          <stop offset="0" stop-color="var(--navy-deep)"/>
          <stop offset="1" stop-color="var(--navy)"/>
        </linearGradient>
        <linearGradient id="whiteField" x1="0" y1="0" x2="1" y2="1">
          <stop offset="0" stop-color="var(--panel-mist)"/>
          <stop offset="0.5" stop-color="var(--panel-white)"/>
          <stop offset="1" stop-color="var(--panel-mist)"/>
        </linearGradient>
        <linearGradient id="lowerFacet" x1="0" y1="0" x2="1" y2="1">
          <stop offset="0" stop-color="var(--steel-blue)"/>
          <stop offset="1" stop-color="var(--navy-deep)"/>
        </linearGradient>
        <radialGradient id="gemGlow" cx="0.5" cy="0.45" r="0.55">
          <stop offset="0" stop-color="#eef2ff"/>
          <stop offset="0.55" stop-color="var(--ice)"/>
          <stop offset="1" stop-color="var(--steel-blue)" stop-opacity="0"/>
        </radialGradient>
      </defs>

      <rect class="field-navy" x="0" y="0" width="800" height="262" fill="url(#navyField)"/>
      <polygon class="facet-lower" points="450,130 800,262 325,262" fill="url(#lowerFacet)"/>
      <polygon class="field-white" points="0,0 325,0 450,130 325,262 0,262" fill="url(#whiteField)"/>

      <ellipse class="gem-photo" role="img" aria-label="Large sparkling blue-white cut diamond photograph"
               cx="595" cy="140" rx="185" ry="130" fill="url(#gemGlow)"/>

      <text class="brand-name" x="158" y="145" text-anchor="middle" font-size="46">VELLA</text>
      <text class="brand-name" x="158" y="168" text-anchor="middle" font-size="13" letter-spacing="6">JEWELERS</text>
    </svg>
  </section>
</main>
</body>
</html>
```